Building Custom Homes

We need a new business card design for a new company called " T & R Custom Homes" . We built custom homes according to our client's dream home. We would like to see designs that use the color blue, green, yellow, orange, pink depicting a home happy 'n bright!

Industry/Entity Type

Business

Contact Information for Business Card

Email: porvina73@quellmail.com.au Mobile: 0438 712 946 Phone: 02 6619 3874 Address: Shop 3 / 17 Wendover Lane Coffs Harbour, NSW 2450 Builders License Number : 47 18 3K ABN : 53 917 648 204 Name: Owen Padick

Colors
0355a3
0392cd
9bcb3c
e34297
f78f20
fbed22

Requirements
Must have
• The Company Name : "T & R Custom Homes"
• must depict the building industry

```html
<!DOCTYPE html>
<html lang="en">
<head>
<meta charset="UTF-8">
<title>T &amp; R Custom Homes – Business Card</title>
<link rel="stylesheet" href="https://fonts.googleapis.com/css2?family=Questrial&display=swap">
<style>
  :root {
    --paint-violet: #5b5a80;
    --paint-slate: #4c5868;
    --paint-olive: #7c8460;
    --paint-moss: #5f7058;
    --paint-plum: #6a4f78;
    --house-shade: #454c52;
    --house-wall: #6d7266;
    --name-white: #ffffff;
    --role-yellow: #f4ea1e;
    --label-cyan: #2ed3e6;
    --stripe-green: #4cf200;
    --stripe-orange: #f78f20;
    --stripe-teal: #12928f;
    --stripe-pink: #ff1c8c;
    --stripe-yellow: #fbed22;
    --stripe-blue: #0392cd;
    --wordmark: #ffffff;
  }
  * { margin: 0; padding: 0; box-sizing: border-box; }
  html, body {
    width: 1200px;
    height: 686px;
    overflow: hidden;
    background: #ffffff;
  }
  .card {
    position: relative;
    width: 1200px;
    height: 686px;
    overflow: hidden;
    font-family: "Questrial", "Century Gothic", sans-serif;
  }
  .card__backdrop {
    position: absolute;
    inset: 0;
    background:
      radial-gradient(ellipse 420px 300px at 180px 420px, rgba(80, 90, 95, 0.75), transparent 70%),
      radial-gradient(ellipse 380px 320px at 620px 260px, rgba(124, 132, 96, 0.7), transparent 70%),
      radial-gradient(ellipse 300px 260px at 900px 120px, rgba(106, 79, 120, 0.7), transparent 70%),
      linear-gradient(135deg, var(--paint-violet) 0%, var(--paint-slate) 35%, var(--paint-moss) 60%, var(--paint-plum) 100%);
  }
  .card__house {
    position: absolute;
    left: 28px;
    top: 266px;
    width: 290px;
    height: 196px;
    border-radius: 6px;
    background: linear-gradient(180deg, var(--house-shade) 0%, var(--house-shade) 40%, var(--house-wall) 100%);
    opacity: 0.75;
  }
  .card__stripes {
    position: absolute;
    inset: 0;
    width: 1200px;
    height: 686px;
  }
  .identity {
    position: absolute;
    left: 52px;
    top: 104px;
  }
  .identity__name {
    color: var(--name-white);
    font-size: 51px;
    line-height: 1;
    letter-spacing: 1.5px;
    font-weight: 400;
  }
  .identity__role {
    margin-top: 6px;
    color: var(--role-yellow);
    font-size: 37px;
    line-height: 1;
    font-weight: 400;
  }
  .identity__contacts {
    margin-top: 10px;
    list-style: none;
    color: var(--label-cyan);
    font-size: 25px;
    line-height: 37px;
  }
  .wordmark {
    position: absolute;
    left: 724px;
    top: 330px;
    transform: translate(-50%, -50%) rotate(-33deg);
    white-space: nowrap;
    color: var(--wordmark);
    font-size: 84px;
    line-height: 1;
    font-weight: 400;
  }
</style>
</head>
<body>
  <main class="card">
    <div class="card__backdrop" role="img" aria-label="Painted abstract backdrop in violet, slate and olive tones"></div>
    <div class="card__house" role="img" aria-label="Faint illustration of a two-gable house showing the building trade"></div>

    <svg class="card__stripes" viewBox="0 0 1200 686" aria-hidden="true">
      <g transform="translate(1200 686) rotate(-34)">
        <rect class="stripe" x="-1500" y="-506" width="1800" height="30" fill="var(--stripe-green)"/>
        <rect class="stripe" x="-1500" y="-476" width="1800" height="14" fill="var(--stripe-teal)"/>
        <rect class="stripe" x="-1500" y="-462" width="1800" height="40" fill="var(--stripe-orange)"/>
        <rect class="stripe" x="-1500" y="-422" width="1800" height="18" fill="var(--stripe-green)"/>
        <rect class="stripe" x="-1500" y="-404" width="1800" height="34" fill="var(--stripe-teal)"/>
        <rect class="stripe" x="-1500" y="-370" width="1800" height="20" fill="var(--stripe-pink)"/>
        <rect class="stripe" x="-1500" y="-350" width="1800" height="36" fill="var(--stripe-orange)"/>
        <rect class="stripe" x="-1500" y="-314" width="1800" height="16" fill="var(--stripe-yellow)"/>
        <rect class="stripe" x="-1500" y="-298" width="1800" height="30" fill="var(--stripe-teal)"/>
        <rect class="stripe" x="-1500" y="-268" width="1800" height="22" fill="var(--stripe-green)"/>
        <rect class="stripe" x="-1500" y="-246" width="1800" height="30" fill="var(--stripe-pink)"/>
        <rect class="stripe" x="-1500" y="-216" width="1800" height="18" fill="var(--stripe-yellow)"/>
        <rect class="stripe" x="-1500" y="-198" width="1800" height="34" fill="var(--stripe-orange)"/>
        <rect class="stripe" x="-1500" y="-164" width="1800" height="20" fill="var(--stripe-blue)"/>
        <rect class="stripe" x="-1500" y="-144" width="1800" height="26" fill="var(--stripe-green)"/>
        <rect class="stripe" x="-1500" y="-118" width="1800" height="22" fill="var(--stripe-pink)"/>
        <rect class="stripe" x="-1500" y="-96" width="1800" height="28" fill="var(--stripe-yellow)"/>
        <rect class="stripe" x="-1500" y="-68" width="1800" height="24" fill="var(--stripe-orange)"/>
        <rect class="stripe" x="-1500" y="-44" width="1800" height="20" fill="var(--stripe-teal)"/>
        <rect class="stripe" x="-1500" y="-24" width="1800" height="60" fill="var(--stripe-pink)"/>
      </g>
    </svg>

    <section class="identity">
      <h1 class="identity__name">DARVEN ELLIS MORANTE</h1>
      <p class="identity__role">INTERIOR DESIGNER</p>
      <ul class="identity__contacts">
        <li class="identity__contact">Contact:</li>
        <li class="identity__contact">Email:</li>
      </ul>
    </section>

    <p class="wordmark">T &amp; R Custom Homes</p>
  </main>
</body>
</html>
```